LEARN Business Skills so you can Earn a good living

size of the poster is 8”x 10.75" plus 0.25" bleed.
Please leave 1 inch on the bottoum for footer
I want a design a poster that will attract people's attention.
I appreciate a creative ad however the ad should not take away from being able to clearly read the text.
-I also appreciate a simple creative ad that is not too busy.
-you can use graphics, vectors, or pictures of real people.
-however, if you use real people it should be a white male that is wearing a white shirt and look like a professional person.

Target Market(s)

Potential young business people

Industry/Entity Type

education

Requirements
Must have
• easy to read the text
Nice to have
• I would like a "creative" simple ad that is easy to be read
Should not have
• pictures of women

```html
<!DOCTYPE html>
<html lang="en">
<head>
<meta charset="utf-8">
<title>Learn It To Earn It – Business Enrichment Course</title>
<link rel="stylesheet" href="https://fonts.googleapis.com/css2?family=Bebas+Neue&family=Roboto+Condensed:wght@400;500;700&family=Roboto:wght@400;500&display=swap">
<style>
  :root {
    --navy: #12306b;
    --navy-deep: #0c2458;
    --gold: #d4b400;
    --gold-dark: #c9a600;
    --cyan: #29b6e8;
    --green: #4cb52e;
    --ink: #222a35;
    --white: #ffffff;
    --stage: #eef0f2;
    --paper-grey: #d9dbdf;
  }
  * { box-sizing: border-box; margin: 0; padding: 0; }
  html, body {
    width: 1200px; height: 1200px; overflow: hidden;
    background: var(--stage);
  }
  .poster {
    position: absolute; left: 180px; top: 36px;
    width: 840px; height: 1128px;
    background: linear-gradient(100deg, var(--white) 35%, var(--paper-grey) 100%);
    overflow: hidden;
    box-shadow: 0 4px 18px rgba(0,0,0,.15);
  }
  .header-shape { position: absolute; left: 0; top: 0; width: 840px; height: 420px; }
  .headline {
    position: absolute; left: 40px; top: 62px;
    font-family: "Bebas Neue", sans-serif;
    font-size: 150px; line-height: 0.84;
    color: var(--white);
    text-shadow: 4px 5px 6px rgba(0,0,0,.35);
  }
  .headline .accent { color: var(--gold); }
  .model-photo {
    position: absolute; left: 530px; top: 95px;
    width: 310px; height: 790px;
    background: linear-gradient(180deg, #7a5a44 0%, #c89e86 22%, #e9edf7 34%, #dfe4f0 80%, #3a3d44 100%);
    border-radius: 140px 140px 0 0;
  }
  .course-title {
    position: absolute; left: 32px; top: 440px;
    font-family: "Bebas Neue", sans-serif;
    font-size: 138px; line-height: 1;
    color: var(--navy);
  }
  .course-band {
    position: absolute; left: 0; top: 552px;
    width: 450px; height: 62px;
    background: var(--cyan);
    clip-path: polygon(0 0, 100% 0, 96% 100%, 0 100%);
    font-family: "Bebas Neue", sans-serif;
    font-size: 62px; line-height: 66px;
    color: var(--white);
    padding-left: 34px;
  }
  .tagline {
    position: absolute; left: 40px; top: 630px;
    font-family: "Roboto Condensed", sans-serif;
    font-size: 28px; line-height: 1.35;
    color: var(--ink);
  }
  .skills-pill {
    position: absolute; left: 40px; top: 725px;
    width: 358px; height: 36px;
    background: var(--green); border-radius: 8px;
    font-family: "Roboto Condensed", sans-serif; font-weight: 700;
    font-size: 24px; line-height: 36px;
    color: var(--white); padding-left: 12px;
  }
  .benefit-lead {
    position: absolute; left: 40px; top: 768px;
    font-family: "Roboto Condensed", sans-serif; font-weight: 700;
    font-size: 42px; line-height: 1.1;
    color: var(--navy);
  }
  .benefit-lead .green { color: var(--green); }
  .benefit-detail {
    position: absolute; left: 40px; top: 820px;
    font-family: "Roboto Condensed", sans-serif;
    font-size: 27px; line-height: 1.1;
    color: var(--ink);
  }
  .topics {
    position: absolute; left: 0; top: 884px;
    width: 840px; height: 132px;
    background: var(--navy);
    padding: 13px 28px 0 26px;
    font-family: "Roboto", sans-serif;
    font-size: 16px; line-height: 21.5px;
    color: var(--white);
    text-transform: uppercase;
  }
  .topic-line { display: flex; justify-content: space-between; white-space: nowrap; }
  .topic-line.short { justify-content: flex-start; gap: 10px; }
  .dot { color: var(--gold); }
  .footer-space { position: absolute; left: 0; top: 1016px; width: 840px; height: 112px; background: var(--white); }
</style>
</head>
<body>
<div class="poster">
  <svg class="header-shape" viewBox="0 0 840 420" aria-hidden="true">
    <defs>
      <radialGradient id="headerGlow" cx="0.7" cy="0.2" r="0.8">
        <stop offset="0" stop-color="#1d4590"/>
        <stop offset="1" stop-color="#0c2458"/>
      </radialGradient>
    </defs>
    <polygon points="0,258 240,418 840,196 840,220 248,438 0,282" fill="#c9a600"/>
    <polygon points="0,0 840,0 840,196 240,418 0,258" fill="#d4b400"/>
    <polygon points="0,0 840,0 840,176 240,398 0,250" fill="url(#headerGlow)"/>
  </svg>

  <div class="headline">LEARN IT<br>TO <span class="accent">EARN IT</span></div>

  <div class="model-photo" role="img" aria-label="Smiling young professional man in a white shirt giving a thumbs up and holding a laptop"></div>

  <div class="course-title">BUSINESS</div>
  <div class="course-band">ENRICHMENT COURSE</div>

  <p class="tagline">A proven success of helping<br>people in their livelihoods</p>

  <div class="skills-pill">Business skills that will help you:</div>
  <div class="benefit-lead"><span class="green">GET A</span> QUALITY JOB</div>
  <p class="benefit-detail">start/grow your business-In-<br>crease your salary</p>

  <div class="topics">
    <div class="topic-line"><span><span class="dot">•</span> Business Administration</span><span><span class="dot">•</span> Small Business Management</span><span><span class="dot">•</span> Finance</span><span><span class="dot">•</span> Investments</span></div>
    <div class="topic-line"><span><span class="dot">•</span> Computers <span class="dot">•</span> Accounting <span class="dot">•</span> Sales <span class="dot">•</span> Marketing <span class="dot">•</span> Project Management</span><span>Interviewing</span></div>
    <div class="topic-line"><span>&nbsp;&nbsp;Skills <span class="dot">•</span> Business Law <span class="dot">•</span> Negotiation <span class="dot">•</span> Public Speaking <span class="dot">•</span> Import/Export <span class="dot">•</span></span><span>Information</span></div>
    <div class="topic-line"><span><span class="dot">•</span> Technology <span class="dot">•</span> Distribution</span><span><span class="dot">•</span> Marketing <span class="dot">•</span> Ledgerly <span class="dot">•</span> Real Estate <span class="dot">•</span></span><span>Health Care</span></div>
    <div class="topic-line short"><span><span class="dot">•</span> Management <span class="dot">•</span> MarketHub</span></div>
  </div>

  <div class="footer-space"></div>
</div>
</body>
</html>
```